RM Skyline Imaging Web Site design

I am looking for a responsive single page website deign for rmskylineimages.com. This is a drone based RM Skyline Imaging and cinematography business. It should have an about us section, a services section that contains photograph service, Video footage, and Aerial mapping all under the services section, a pricing section, and then a contact page for customers to contact us.

Coding

Coded - Design and coding required

Number of Pages Required

1 page

Font styles to use
Sans Serif

Colors

Designer to choose colors to be used in the design.

Requirements
Must have
• Responsive design. About us section, services section, pricing section under the services links, and contact us section, that links to a submission page where they can send Name, address, email, and comments on what they are interested in.
• See hoverlens7.com - looking for similar design.
Should not have
• clutter, or too busy design

```html
<!DOCTYPE html>
<html lang="en">
<head>
<meta charset="utf-8">
<title>RM Skyline Imaging</title>
<link rel="stylesheet" href="https://fonts.googleapis.com/css2?family=Montserrat:wght@400;500;600&family=Gelasio:wght@400;500&display=swap">
<style>
:root{
  --navy:#1f2a68;
  --ink:#1c2a6b;
  --orange:#f7931e;
  --white:#ffffff;
  --muted:#eef1f6;
  --sans:"Montserrat", Arial, sans-serif;
  --serif:"Gelasio", Georgia, serif;
}
*{box-sizing:border-box;margin:0;padding:0}
html,body{width:1200px;height:2278px;overflow:hidden;background:var(--white)}
body{position:relative;font-family:var(--sans);color:var(--ink)}
.abs{position:absolute}

/* hero */
.hero{left:0;top:0;width:1200px;height:656px;
  background:linear-gradient(160deg,#4a4440 0%,#5d554f 35%,#3e3a38 70%,#2f2c2b 100%)}
.brand{left:160px;top:40px;display:flex;align-items:center;gap:10px;color:var(--white);font-size:15px;font-weight:500;letter-spacing:4px}
.brand-dot{width:14px;height:14px;border-radius:50%;background:var(--orange)}
.nav{left:709px;top:48px;display:flex;gap:32px}
.nav a{color:var(--white);text-decoration:none;font-size:13px;font-weight:600}
.hero-title{right:160px;top:228px;text-align:right;color:var(--white);font-size:42px;font-weight:600;line-height:60px}
.btn{top:383px;width:176px;height:50px;border:2px solid var(--white);color:var(--white);font-size:13px;font-weight:500;display:flex;align-items:center;justify-content:center}
.btn-learn{left:673px}
.btn-contact{left:864px}

/* about */
.section-label{font-size:13px;font-weight:500;display:flex;align-items:center;gap:10px}
.about-label{left:264px;top:733px;color:var(--ink)}
.about-label .arrow{color:#3a7bff}
.about-text{left:264px;top:786px;width:660px;height:172px;overflow:hidden;font-family:var(--serif);font-size:26px;line-height:43px;color:var(--ink)}

/* services */
.services{left:0;top:1028px;width:1200px;height:569px;
  background:linear-gradient(180deg,#6a625c 0%,#776e66 40%,#4d4641 100%)}
.services-label{left:264px;top:1105px;color:var(--white)}
.svc-icon{width:275px;height:202px;top:1180px;background:var(--orange);display:flex;justify-content:center;padding-top:50px}
.svc-card{width:229px;height:170px;top:1346px;background:var(--white);border-top:4px solid var(--navy);padding:16px 19px}
.svc-kicker{font-size:9px;color:var(--orange);font-weight:500;text-transform:uppercase}
.svc-name{font-family:var(--serif);font-size:21px;margin:12px 0 14px}
.svc-desc{font-size:10.5px;line-height:20px}

/* pricing */
.pricing-title{left:0;top:1645px;width:1200px;text-align:center;font-family:var(--serif);font-size:30px;color:var(--orange)}
.price-card{top:1722px;width:228px;height:228px;text-align:center;padding:40px 10px 0}
.price-city{left:235px;background:linear-gradient(160deg,#e9ebee,#cfd3d8)}
.price-field{left:486px;background:linear-gradient(160deg,#bcd39a,#d8e0cf)}
.price-mesh{left:738px;background:linear-gradient(160deg,#d7e1e4,#b8c4c9)}
.price-amount{font-family:var(--serif);font-size:46px;font-weight:500;line-height:46px;color:var(--ink)}
.price-line{font-family:var(--serif);font-size:20px;line-height:26px;margin-top:6px}
.price-desc{font-size:10.5px;line-height:14px;margin-top:10px}

/* footer */
.footer{left:0;top:2029px;width:1200px;height:249px;background:var(--navy);color:var(--white)}
.foot-rule{left:160px;top:2096px;width:250px;height:1px;background:#8b93bf}
.foot-nav{left:160px;top:2111px;display:flex;gap:22px;font-family:var(--serif);font-size:13px}
.foot-contact{left:160px;top:2154px;font-size:11px;line-height:25px}
.copyright{left:160px;top:2238px;font-size:11px}
.field{border:1px solid #c9cde3;height:39px;font-size:11px;padding:12px 12px;color:var(--white)}
.send{border-color:var(--orange);color:var(--orange);text-align:center}
.social{top:2236px;width:16px;height:16px;border-radius:50%;background:var(--white)}
</style>
</head>
<body>

<div class="abs hero" role="img" aria-label="Aerial photo of a dense downtown skyline seen from above"></div>
<div class="abs brand"><span class="brand-dot"></span>RM Skyline Imaging</div>
<nav class="abs nav"><a>About Us</a><a>Services</a><a>Pricing</a><a>Contact Us</a></nav>
<h1 class="abs hero-title">RM Skyline<br>Imaging</h1>
<div class="abs btn btn-learn">Learn More</div>
<div class="abs btn btn-contact">Contact Us</div>

<div class="abs section-label about-label">About Us <span class="arrow">→</span></div>
<p class="abs about-text">You have an idea and a need. RM Skyline Imaging has the skills and desire to help. A team, a collaborative partnership is waiting to be formed. Do you have a home, a large parcel, a sprawling ranch, or a com-</p>

<div class="abs services" role="img" aria-label="Aerial view of a city skyline with a tall spire tower"></div>
<div class="abs section-label services-label">Our Services <span>→</span></div>

<div class="abs svc-icon" style="left:160px">
  <svg width="84" height="66" viewBox="0 0 84 66" fill="none" stroke="#fff" stroke-width="4" stroke-linejoin="round"><path d="M4 16h18l6-10h28l6 10h18v46H4z"/><circle cx="42" cy="38" r="14"/><circle cx="14" cy="26" r="1.5" fill="#fff"/></svg>
</div>
<div class="abs svc-card" style="left:182px">
  <div class="svc-kicker">Aerial Photography</div>
  <div class="svc-name">Photograph Service</div>
  <div class="svc-desc">Drone Photography services include editing, titling, and more.</div>
</div>

<div class="abs svc-icon" style="left:462px">
  <svg width="84" height="76" viewBox="0 0 84 76" fill="none" stroke="#fff" stroke-width="4" stroke-linejoin="round"><circle cx="24" cy="12" r="9"/><circle cx="46" cy="12" r="9"/><rect x="12" y="24" width="44" height="30" rx="3"/><path d="M56 32l20-10v34L56 46"/><path d="M22 36h22M18 62h34M35 54v8"/></svg>
</div>
<div class="abs svc-card" style="left:484px">
  <div class="svc-kicker">Aerial Photography</div>
  <div class="svc-name">Video Footage</div>
  <div class="svc-desc">Available Drone Videography services include filming, editing, music, titling and more.</div>
</div>

<div class="abs svc-icon" style="left:765px">
  <svg width="130" height="66" viewBox="0 0 130 66" fill="none" stroke="#fff" stroke-width="3" stroke-linejoin="round"><path d="M65 3l62 30-62 30L3 33z"/><path d="M34 18l62 30M96 18L34 48M49 10l62 30M81 10L19 40M19 26l62 30M111 26L49 56"/></svg>
</div>
<div class="abs svc-card" style="left:787px">
  <div class="svc-kicker">Aerial Photography</div>
  <div class="svc-name">Aerial Mapping</div>
  <div class="svc-desc">3D Mapping services include 2D Maps, and 3D Models.</div>
</div>

<h2 class="abs pricing-title">Pricing</h2>
<div class="abs price-card price-city" role="img" aria-label="Faded aerial photo of city towers">
  <div class="price-amount">200</div>
  <div class="price-line">up to 20 edited high resolution images.</div>
  <div class="price-desc">Available Drone Photography services include editing, titling, and more.</div>
</div>
<div class="abs price-card price-field" role="img" aria-label="Faded aerial photo of green fields and houses">
  <div class="price-amount">200</div>
  <div class="price-line">Raw aerial footage available for you to use.</div>
  <div class="price-desc">Available Drone Videography services include filming, editing, music, titling and more.</div>
</div>
<div class="abs price-card price-mesh" role="img" aria-label="Faded 3D terrain mesh model">
  <div class="price-amount">200</div>
  <div class="price-line">3D Model</div>
  <div class="price-desc">Available 3D Mapping services include 2D Maps, and 3D Models.</div>
</div>

<footer class="abs footer"></footer>
<div class="abs foot-rule"></div>
<div class="abs foot-nav"><span>About</span><span>Services</span><span>Pricing</span><span>Contact</span></div>
<div class="abs foot-contact">Tel : 0098-5512470<br>Email : hello@rmskylineimages.com</div>
<div class="abs copyright">© RM Skyline Imaging,</div>

<div class="abs field" style="left:535px;top:2094px;width:242px">Name</div>
<div class="abs field" style="left:781px;top:2094px;width:260px">Address</div>
<div class="abs field" style="left:535px;top:2142px;width:202px">Email</div>
<div class="abs field" style="left:741px;top:2142px;width:202px">Comment</div>
<div class="abs field send" style="left:949px;top:2142px;width:92px">Send</div>

<div class="abs social" style="left:892px" aria-label="Social link"></div>
<div class="abs social" style="left:932px" aria-label="Social link"></div>
<div class="abs social" style="left:976px" aria-label="Social link"></div>
<div class="abs social" style="left:1020px" aria-label="Social link"></div>

</body>
</html>
```